Business Cards

We are wanting business cards created using previous design #36167008 as a starting point.
Info needed on front side:
Employee Name
Title
Email
Phone Number

Info needed on back side: (these are our product lines)
Frac Valves Fishing
Flowback Thru-Tubing
Torque & Test KMVB

please see changes

```html
<!DOCTYPE html>
<html lang="en">
<head>
<meta charset="utf-8">
<title>Business Cards – Dale Whitford</title>
<link href="https://fonts.googleapis.com/css2?family=Montserrat:wght@300;400;500;600;700&display=swap" rel="stylesheet">
<style>
  :root {
    --backdrop: #a3a3a3;
    --card: #1b1b1b;
    --gold: #e0c08e;
    --gold-deep: #b79e74;
    --white: #ffffff;
    --ghost: #212121;
  }
  * { margin: 0; padding: 0; box-sizing: border-box; }
  html, body { width: 1200px; height: 1200px; overflow: hidden; }
  body {
    background: var(--backdrop);
    font-family: "Montserrat", sans-serif;
    position: relative;
  }
  .card {
    position: absolute;
    left: 219px;
    width: 788px;
    height: 473px;
    background: var(--card);
    overflow: hidden;
  }
  .card--front { top: 117px; }
  .card--back { top: 651px; }

  /* front */
  .ghost-mark {
    position: absolute;
    color: var(--ghost);
    font-weight: 700;
    line-height: 1;
    white-space: nowrap;
  }
  .ghost-mark--left { left: 86px; top: 282px; font-size: 44px; }
  .ghost-mark--left small { display: block; font-size: 26px; letter-spacing: 4px; margin-top: 6px; }
  .ghost-mark--right { left: 400px; top: 296px; font-size: 38px; }

  .identity {
    position: absolute;
    right: 416px;
    top: 200px;
    text-align: right;
  }
  .identity__name {
    color: var(--gold);
    font-weight: 700;
    font-size: 26px;
    letter-spacing: 1.6px;
    line-height: 1.2;
  }
  .identity__title {
    color: var(--white);
    font-weight: 600;
    font-size: 20px;
    margin-top: 2px;
  }
  .divider {
    position: absolute;
    left: 393px;
    top: 203px;
    width: 2px;
    height: 72px;
    background: #3a352c;
  }
  .contacts {
    position: absolute;
    left: 409px;
    top: 201px;
    list-style: none;
  }
  .contacts li {
    display: flex;
    align-items: center;
    height: 25px;
    color: var(--white);
    font-weight: 300;
    font-size: 18.5px;
  }
  .contacts svg { width: 15px; height: 15px; margin-right: 10px; flex: none; }
  .contacts .accent { color: var(--gold); font-weight: 500; }
  .address {
    position: absolute;
    left: 0; right: 0;
    top: 411px;
    text-align: center;
    color: var(--white);
    font-weight: 300;
    font-size: 18.5px;
  }

  /* back */
  .brand {
    position: absolute;
    top: 170px;
    width: 220px;
    text-align: center;
    color: var(--gold);
    font-weight: 700;
    font-size: 24px;
    line-height: 1.2;
  }
  .brand--left { left: 174px; }
  .brand--right { left: 380px; }
  .product-lines {
    position: absolute;
    left: 71px;
    top: 315px;
    width: 644px;
    height: 32px;
    padding: 0 8px;
    border: 1.5px solid var(--gold);
    border-radius: 4px;
    display: flex;
    align-items: center;
    justify-content: space-between;
    color: var(--white);
    font-weight: 500;
    font-size: 18px;
    white-space: nowrap;
  }
  .product-lines .bullet {
    width: 7px; height: 7px; border-radius: 50%;
    background: var(--gold-deep);
    flex: none;
  }
</style>
</head>
<body>
  <section class="card card--front">
    <div class="ghost-mark ghost-mark--left">CORVANE<small>DOWNHOLE LLC</small></div>
    <div class="ghost-mark ghost-mark--right">SUMMIT FLOW</div>

    <div class="identity">
      <div class="identity__name">DALE WHITFORD</div>
      <div class="identity__title">Director</div>
    </div>
    <div class="divider"></div>
    <ul class="contacts">
      <li>
        <svg viewBox="0 0 24 24" fill="none" stroke="#e0c08e" stroke-width="2"><path d="M5 3h4l2 5-3 2a12 12 0 0 0 6 6l2-3 5 2v4a2 2 0 0 1-2 2A18 18 0 0 1 3 5a2 2 0 0 1 2-2z"/></svg>
        +1 415 555 0187
      </li>
      <li>
        <svg viewBox="0 0 24 24" fill="none" stroke="#e0c08e" stroke-width="2"><rect x="3" y="6" width="18" height="13"/><path d="M3 6l9 7 9-7"/></svg>
        hello@northfieldco.com
      </li>
      <li>
        <svg viewBox="0 0 24 24" fill="none" stroke="#e0c08e" stroke-width="1.8"><circle cx="12" cy="12" r="9"/><path d="M3 12h18M12 3c3 3 3 15 0 18M12 3c-3 3-3 15 0 18"/></svg>
        <span>www.<span class="accent">northfieldco</span>.com</span>
      </li>
    </ul>
    <div class="address">12 Harlow Lane 3rd Floor Bristol BS1 4QT, United Kingdom</div>
  </section>

  <section class="card card--back">
    <div class="brand brand--left">CORVANE<br>DOWNHOLE LLC</div>
    <div class="brand brand--right">SUMMIT FLOW<br>SERVICES</div>
    <div class="product-lines">
      <span>Frac Valves Fishing</span><span class="bullet"></span>
      <span>Flowback Thru-Tubing</span><span class="bullet"></span>
      <span>Torque &amp; Test KMVB</span>
    </div>
  </section>
</body>
</html>
```